Dawnfeather… Professional Window Cleaners

Dawnfeather… offers a professional window cleaning service, using both traditional methods and high-performance pure water cleaning system ensuring consistently high results that will last longer, keeping the presentation of your business or home at its peak.

Target Market(s)

Commercial businesses and houses

Colors
0094D4
00A9DD
6FCCEA
C7EBF8
E9F6FB

Requirements
Must have
• Modern window cleaning equipment in the pictures include water feed pole system, I use the "Stride and Gleam" system (logo available) from Velmar window cleaning
Nice to have
• Modern window cleaning tools such as Tallcroft, Span-go, Velmar
Should not have
• DIY picture of cleaning applications, it needs to show professional equipment being used.

```html
<!DOCTYPE html>
<html lang="en">
<head>
<meta charset="utf-8">
<title>Dawnfeather… Professional Window Cleaning Flyer</title>
<link href="https://fonts.googleapis.com/css2?family=Montserrat:wght@300;400;500&family=Rubik:wght@400;500;700;800;900&display=swap" rel="stylesheet">
<style>
  :root {
    --brand-blue: #0094D4;
    --sky-blue: #00A9DD;
    --light-blue: #6FCCEA;
    --pale-blue: #C7EBF8;
    --mist-blue: #E9F6FB;
    --ink: #141414;
    --paper: #ffffff;
    --backdrop: #e8e8e8;
    --rule-grey: #9a9a9a;
    --body-text: #333333;
  }
  * { margin: 0; padding: 0; box-sizing: border-box; }
  html, body { width: 1200px; height: 2599px; overflow: hidden; }
  body { background: var(--backdrop); font-family: "Rubik", sans-serif; color: var(--ink); }

  .flyer {
    position: absolute; left: 0; top: 453px;
    width: 1200px; height: 1692px;
    background: var(--paper); overflow: hidden;
    box-shadow: 0 20px 60px rgba(0,0,0,0.18);
  }
  .flyer > * { position: absolute; }

  .hero-photo {
    left: 432px; top: 0; width: 768px; height: 731px;
    background: linear-gradient(90deg, #ffffff 0%, rgba(255,255,255,0) 30%),
                linear-gradient(180deg, var(--mist-blue) 0%, var(--pale-blue) 30%, #8fb2bd 58%, #5d7f8f 72%, var(--pale-blue) 90%, var(--mist-blue) 100%);
  }

  .brand-name {
    left: 56px; top: 58px;
    font-family: "Montserrat", sans-serif; font-weight: 300;
    font-size: 92px; letter-spacing: -2px; color: var(--ink);
  }
  .headline-kicker {
    left: 56px; top: 208px;
    font-weight: 900; font-size: 62px; color: var(--brand-blue); letter-spacing: -1px;
  }
  .headline-main {
    left: 52px; top: 268px;
    font-weight: 900; font-size: 118px; line-height: 0.92; letter-spacing: -2px; color: var(--ink);
  }
  .headline-rule-grey { left: 56px; top: 535px; width: 380px; height: 2px; background: var(--rule-grey); }
  .headline-rule-accent { left: 56px; top: 532px; width: 72px; height: 7px; background: var(--brand-blue); }
  .tagline {
    left: 56px; top: 568px; width: 480px;
    font-family: "Montserrat", sans-serif; font-weight: 400; font-size: 21px; line-height: 1.42; color: var(--body-text);
  }

  .services-band { left: 0; top: 731px; width: 1200px; height: 205px; background: var(--brand-blue); }
  .services-tab {
    left: 72px; top: 704px; width: 366px; height: 70px;
    background: var(--ink); color: #fff;
    font-weight: 500; font-size: 44px; line-height: 70px; padding-left: 46px;
  }
  .services-tab::before, .services-tab::after {
    content: ""; position: absolute; top: 0; width: 0; height: 0;
    border-top: 27px solid transparent;
  }
  .services-tab::before { left: -24px; border-right: 24px solid var(--ink); }
  .services-tab::after { right: -24px; border-left: 24px solid var(--ink); }

  .service-item {
    top: 818px; display: flex; align-items: flex-start; gap: 12px;
    color: #fff; font-size: 24px; line-height: 1.2; font-weight: 400;
  }
  .service-item svg { margin-top: 6px; flex: none; }
  .service-divider { top: 784px; width: 1px; height: 128px; background: var(--pale-blue); opacity: 0.7; }

  .gallery-tile { top: 982px; width: 331px; height: 194px; }
  .tile-facade { left: 61px; background: linear-gradient(160deg, #9aa9ad 0%, #5c6a70 45%, #2f3a40 100%); }
  .tile-aircraft { left: 438px; background: linear-gradient(180deg, #aebdca 0%, #d6dde3 50%, #6f7275 75%, #8a8b8c 100%); }
  .tile-solar { left: 808px; background: radial-gradient(circle at 22% 25%, #ffffff 0%, var(--light-blue) 12%, var(--brand-blue) 45%, #0a4ea8 100%); }

  .feature-heading {
    left: 61px; top: 1222px; width: 930px;
    font-weight: 700; font-size: 29px; line-height: 1.18; color: var(--ink);
  }
  .feature-copy {
    top: 1318px; width: 482px;
    font-family: "Montserrat", sans-serif; font-size: 17px; line-height: 1.3; color: var(--body-text);
  }
  .copy-left { left: 63px; }
  .copy-right { left: 597px; width: 525px; }

  .footer-bar { left: 0; top: 1528px; width: 1200px; height: 164px; background: var(--ink); }
  .cta-bar {
    left: 56px; top: 1477px; width: 1078px; height: 96px;
    background: var(--sky-blue); border-radius: 4px;
    color: #fff; font-weight: 700; font-size: 22px; line-height: 1.4;
    display: flex; align-items: center; justify-content: center; text-align: center;
  }
  .contact-row {
    left: 64px; top: 1607px; width: 1100px; height: 44px;
    display: flex; align-items: center; color: #fff;
    font-family: "Montserrat", sans-serif;
  }
  .contact-item { display: flex; align-items: center; gap: 12px; }
  .contact-phone { font-size: 32px; font-weight: 400; width: 275px; }
  .contact-web { font-size: 17px; width: 425px; }
  .contact-place { font-size: 17px; }
</style>
</head>
<body>
  <main class="flyer">
    <div class="hero-photo" role="img" aria-label="Photo of professional cleaners washing a tall glass window wall with a water-fed pole system"></div>

    <div class="brand-name">Dawnfeather…</div>
    <div class="headline-kicker">PROFESSIONAL</div>
    <h1 class="headline-main">window<br>cleaning</h1>
    <div class="headline-rule-grey"></div>
    <div class="headline-rule-accent"></div>
    <p class="tagline">Professional High-tech Window Cleaning Solutions, Commercial, Residential, Marine and Aviation.</p>

    <div class="services-band"></div>
    <h2 class="services-tab">our services</h2>

    <div class="service-item" style="left:61px">
      <svg width="22" height="22" viewBox="0 0 22 22"><circle cx="11" cy="11" r="9.5" fill="none" stroke="#fff" stroke-width="1.6"/><path d="M6.5 11.2l3 3 6-6" fill="none" stroke="#fff" stroke-width="1.8"/></svg>
      <span>Pure Water<br>Cleaning</span>
    </div>
    <div class="service-divider" style="left:261px"></div>
    <div class="service-item" style="left:291px">
      <svg width="22" height="22" viewBox="0 0 22 22"><circle cx="11" cy="11" r="9.5" fill="none" stroke="#fff" stroke-width="1.6"/><path d="M6.5 11.2l3 3 6-6" fill="none" stroke="#fff" stroke-width="1.8"/></svg>
      <span>Commercial<br>&amp; Domestic</span>
    </div>
    <div class="service-divider" style="left:504px"></div>
    <div class="service-item" style="left:528px">
      <svg width="22" height="22" viewBox="0 0 22 22"><circle cx="11" cy="11" r="9.5" fill="none" stroke="#fff" stroke-width="1.6"/><path d="M6.5 11.2l3 3 6-6" fill="none" stroke="#fff" stroke-width="1.8"/></svg>
      <span>Glass &amp;<br>Facade</span>
    </div>
    <div class="service-divider" style="left:691px"></div>
    <div class="service-item" style="left:715px">
      <svg width="22" height="22" viewBox="0 0 22 22"><circle cx="11" cy="11" r="9.5" fill="none" stroke="#fff" stroke-width="1.6"/><path d="M6.5 11.2l3 3 6-6" fill="none" stroke="#fff" stroke-width="1.8"/></svg>
      <span>Aviation &amp;<br>Marine</span>
    </div>
    <div class="service-divider" style="left:899px"></div>
    <div class="service-item" style="left:933px">
      <svg width="22" height="22" viewBox="0 0 22 22"><circle cx="11" cy="11" r="9.5" fill="none" stroke="#fff" stroke-width="1.6"/><path d="M6.5 11.2l3 3 6-6" fill="none" stroke="#fff" stroke-width="1.8"/></svg>
      <span>Solar Panel<br>Cleaning</span>
    </div>

    <div class="gallery-tile tile-facade" role="img" aria-label="Photo of a commercial glass shopfront reflecting a car park"></div>
    <div class="gallery-tile tile-aircraft" role="img" aria-label="Photo of a private jet parked on an airfield"></div>
    <div class="gallery-tile tile-solar" role="img" aria-label="Photo of blue solar panels under a bright sun"></div>

    <h3 class="feature-heading">Commercial, Domestic Glass Cleaning – perfect results every<br>time from Dawnfeather…</h3>
    <p class="feature-copy copy-left">Dawnfeather… offers a professional window cleaning service, using both traditional methods and high-performance pure water cleaning system ensuring consistently high results that will last longer, keeping the presentation of your business or home at its peak.</p>
    <p class="feature-copy copy-right">Regular office and home window cleaning will not only improve the appearance of your business and home, having clean windows creates better natural light that promotes improved mood, and ultimately better productivity by making rooms appear more spacious and inviting.</p>

    <div class="footer-bar"></div>
    <div class="cta-bar">SPEAK WITH DAWNFEATHER… PROFESSIONAL WINDOW CLEANING<br>ABOUT SCHEDULED OR SINGLE VISIT OPTIONS.</div>

    <div class="contact-row">
      <div class="contact-item contact-phone">
        <svg width="24" height="24" viewBox="0 0 24 24"><path d="M6.5 3.5l3 3.2-1.8 2.4c1.2 2.6 3.4 4.8 6 6l2.4-1.8 3.2 3-1.8 3c-7.6-.4-13.6-6.4-14-14z" fill="none" stroke="#fff" stroke-width="1.5" stroke-linejoin="round"/></svg>
        <span>0400 628 317</span>
      </div>
      <div class="contact-item contact-web">
        <svg width="22" height="22" viewBox="0 0 22 22"><circle cx="11" cy="11" r="9" fill="none" stroke="#fff" stroke-width="1.4"/><ellipse cx="11" cy="11" rx="4" ry="9" fill="none" stroke="#fff" stroke-width="1.2"/><path d="M2 11h18" stroke="#fff" stroke-width="1.2"/></svg>
        <span>dawnfeatherwindows.example.com</span>
      </div>
      <div class="contact-item contact-place">
        <svg width="18" height="22" viewBox="0 0 18 22"><path d="M9 21s-7-7.2-7-12a7 7 0 0114 0c0 4.8-7 12-7 12z" fill="none" stroke="#fff" stroke-width="1.5"/><circle cx="9" cy="9" r="2.6" fill="none" stroke="#fff" stroke-width="1.4"/></svg>
        <span>Harbourvale Western Australia 6099</span>
      </div>
    </div>
  </main>
</body>
</html>
```